Web Card Landing Page Template Site

Our company sells "be found online" packages. We submit key information about a business to major data aggregators in the USA. One of the things we submit is a domain name. So we are selling a custom domain name which will be used with a one page web card site that is has local search markup built in and is Responsive.

I am looking for a new responsive simple design from pixel forge optimized for search engines, desktops and mobile devices.
We sell high quantities of this package and I want to be able to change out new business information quickly in our WordPress Multi-site environment. Commented code is a must. The color layout should be neutral to fit many types of businesses.

Necessary areas on template:
Main Company Logo
Up to 5 images from customer
Business Name
Full Address
Main Phone
Toll Free
Cell Phone
Fax
email address
Website
Hours of operation
types of payments accepted (example: Keystone Card | Vantage | Meridian | Cash | Check)
up to 5 categories (example:Auto Repair | Mechanic | Tire Dealers | Breaks | AC Repair)
Area for Business Description (500 or less characters will be used)
Certifications/Memberships/Specialties
year established
Map (should be a map of the business address) (not sure if this can be linked some how)
Social Icons (Google+,Facebook,Twitter,YouTube,LinkedIn)

Our main goal is to have customers visit this business web card from a local search and to find most things there looking for at a glance and want to make a quick decision tor work with the company.
Simple enough for entry level techs or data entry employees to update each new page with new business information.
We look forward to designs. :)
Updates

Please don't hesitate to ask questions regarding this brief.

Participation money available now.

I look forward to feed back from potential designers

Thanks

Also this project is now Committed instead of Refundable.

Ok, Designers, to help clarify, this single page design you create will be used over and over and over again for different types of small businesses. it will mostly be a one size fits all type design. It will need to be used as a template for us to quickly put in new customers data and pictures and then we will point there domain name at the design. One day it could be a plumber company, another day a heating contractor and another day a a beauty salon or an insurance company.

Here is two links of something similar except this design is missing a few necessity things that is listed in my brief. View the source for ideas. I may have to extend this project, keep posted on this project. Thanks

http://brindlecrestdepot.velmarkindex.example/brindlecrest/waste-management
http://quillbrookmediallc.velmarkindex.example/tansy-hollow/yellow-pages

or a sample of images, and some of the necessities to be on this one pager design
http://harvicknearby.example/public_html/wp-admin/images/client-images/Example.PNG

Reason: Designers requested more time. I hope the designers that didn't have the time prior take a second look. Please review the breif with a more clear understanding of scope of work.

• sample of images, and some of the necessities to be on this one pager design

```html
<!DOCTYPE html>
<html lang="en">
<head>
<meta charset="utf-8">
<title>Northvale Service Co — Web Card</title>
<link rel="stylesheet" href="https://fonts.googleapis.com/css2?family=Playfair+Display&family=Crimson+Text&family=Arimo&display=swap">
<style>
  :root {
    --page-bg: #f7f6f1;
    --header-bg: #eeede4;
    --frame: #eeebe2;
    --ink: #2b2a28;
    --body-ink: #3a3a3a;
    --muted: #6a5d50;
    --accent: #8c857c;
    --rule: #9a9890;
    --footer-rule: #e9e8df;
    --brand: #1f6f95;
  }
  * { margin: 0; padding: 0; box-sizing: border-box; }
  html, body { width: 1200px; height: 960px; overflow: hidden; background: var(--page-bg); }
  body { position: relative; font-family: "Crimson Text", Georgia, serif; color: var(--ink); }

  /* Header band */
  .site-header { position: absolute; left: 0; top: 0; width: 1200px; height: 100px; background: var(--header-bg); }
  .brand { position: absolute; left: 81px; top: 36px; display: flex; align-items: center; gap: 10px; }
  .brand-mark { width: 26px; height: 26px; border-radius: 50%; background: var(--brand); }
  .brand-name { font-size: 20px; color: var(--brand); }
  .header-tools { position: absolute; right: 87px; top: 47px; display: flex; align-items: center; font-size: 15px; color: #555; }
  .header-tools .tool { display: flex; align-items: center; gap: 14px; padding: 0 14px; border-left: 1px solid #dcdad0; height: 26px; }
  .header-tools .tool:first-child { border-left: 0; padding-left: 0; }
  .header-tools .phone { color: var(--accent); }
  .caret { width: 10px; height: 6px; }

  /* Gallery */
  .gallery { position: absolute; left: 81px; top: 131px; display: flex; gap: 27px; }
  .gallery-item { width: 240px; height: 198px; background: var(--frame); padding: 10px; }
  .gallery-item .photo { width: 100%; height: 100%; }
  .photo-brushes { background: linear-gradient(135deg, #f4ebe2, #cfe6c8 55%, #f2e8df); }
  .photo-kabuki { background: radial-gradient(circle at 50% 45%, #9fd6c0, #e9e1d7 60%); }
  .photo-bottles { background: linear-gradient(90deg, #e8c8d4, #d993b4 50%, #eed8df); }
  .photo-organic { background: linear-gradient(180deg, #ffffff, #eef0e8 60%, #ffffff); }

  /* Welcome */
  .welcome { position: absolute; left: 81px; top: 360px; width: 1033px; }
  .welcome h1 { font-family: "Playfair Display", Georgia, serif; font-weight: 400; font-size: 37px; line-height: 44px; width: 255px; border-bottom: 1px solid var(--ink); }
  .welcome p { margin-top: 14px; padding-left: 2px; font-family: "Arimo", Arial, sans-serif; font-size: 16px; line-height: 22.5px; color: var(--body-ink); }
  .section-rule { position: absolute; left: 80px; top: 506px; width: 1034px; height: 1px; background: var(--rule); }

  /* Footer columns */
  .footer-col { position: absolute; top: 568px; }
  .footer-col h2 { font-weight: 400; font-size: 19px; line-height: 24px; color: var(--ink); }
  .footer-col ul { list-style: none; margin-top: 30px; font-size: 13px; line-height: 18px; color: var(--muted); }
  .col-info { left: 81px; }
  .col-categories { left: 342px; }
  .col-categories li { padding-left: 18px; position: relative; margin-bottom: 4.5px; }
  .col-categories li::before { content: "›"; position: absolute; left: 0; top: 0; }
  .col-timing { left: 610px; }
  .col-locate { left: 881px; top: 570px; }
  .map { display: block; width: 200px; height: 112px; margin-top: 6px; background: linear-gradient(135deg, #e3e0d8, #d5d2c9 50%, #e6e3db); }
  .col-locate h2.follow { margin-top: 6px; }
  .social { display: flex; gap: 17px; margin-top: 24px; padding-left: 2px; }
  .social span { width: 13px; height: 13px; border-radius: 50%; background: #4a4540; }

  /* Bottom */
  .footer-rule { position: absolute; left: 81px; top: 836px; width: 1041px; height: 5px; background: var(--footer-rule); }
  .copyright { position: absolute; left: 81px; top: 877px; font-size: 14px; color: var(--muted); }
</style>
</head>
<body>
  <header class="site-header">
    <div class="brand">
      <span class="brand-mark"></span>
      <span class="brand-name">Northvale Service Co</span>
    </div>
    <div class="header-tools">
      <div class="tool"><span>Cell phone : <span class="phone">555-284-1937</span></span>
        <svg class="caret" viewBox="0 0 10 6"><path d="M1 1l4 4 4-4" fill="none" stroke="#555" stroke-width="1.4"/></svg></div>
      <div class="tool"><span>En</span>
        <svg class="caret" viewBox="0 0 10 6"><path d="M1 1l4 4 4-4" fill="none" stroke="#555" stroke-width="1.4"/></svg></div>
      <div class="tool"><span>$</span>
        <svg class="caret" viewBox="0 0 10 6"><path d="M1 1l4 4 4-4" fill="none" stroke="#555" stroke-width="1.4"/></svg></div>
    </div>
  </header>

  <section class="gallery">
    <div class="gallery-item"><div class="photo photo-brushes" role="img" aria-label="Set of green bamboo makeup brushes"></div></div>
    <div class="gallery-item"><div class="photo photo-kabuki" role="img" aria-label="Green kabuki brush on a white surface"></div></div>
    <div class="gallery-item"><div class="photo photo-bottles" role="img" aria-label="Three pink body care bottles on a shelf"></div></div>
    <div class="gallery-item"><div class="photo photo-organic" role="img" aria-label="Organic skin care product range"></div></div>
  </section>

  <section class="welcome">
    <h1>Welcome</h1>
    <p>Servicing Brindlecrest, Tansy Hollow, Oakmere, Fennick and Larkvale Since&nbsp; 1990 NTC certified Technicians and A+ TBR rating | Chamber of commerce member Specializing in oil changes, AC repai, brakes, and tires | we carry all major tire brands Satisfaction guaranteed | 1 year warranty on all repair.</p>
  </section>
  <div class="section-rule"></div>

  <div class="footer-col col-info">
    <h2>information</h2>
    <ul>
      <li>48 N Harlow Ave</li>
      <li>Brindlecrest W 50912</li>
      <li>Cell Phone : 555-310-7742</li>
      <li>Toll Free : 888-555-0196</li>
      <li>info@northvaleservice.example</li>
      <li>www.northvaleservice.example</li>
    </ul>
  </div>

  <div class="footer-col col-categories">
    <h2>categories</h2>
    <ul>
      <li>Foundation" Brush Kit</li>
      <li>Green Bamboo Kabuki Brush</li>
      <li>Solvane Glow Tan</li>
      <li>Fennel Seed Oil and Extract</li>
    </ul>
  </div>

  <div class="footer-col col-timing">
    <h2>timing</h2>
    <ul>
      <li>Monday through Friday 8-5</li>
      <li>Saturday 8-8</li>
      <li>Keystone Card | Vantage</li>
      <li>Meridian | Atlas Express</li>
    </ul>
  </div>

  <div class="footer-col col-locate">
    <h2>locate us</h2>
    <div class="map" role="img" aria-label="Street map showing the business location"></div>
    <h2 class="follow">follow us</h2>
    <div class="social">
      <span></span><span></span><span></span><span></span><span></span>
    </div>
  </div>

  <div class="footer-rule"></div>
  <p class="copyright">© 2014 Pixelforge.example. All Rights Reserved.</p>
</body>
</html>
```